Copperleaf Motorized Shade Business Card

Hello, we've had our logo made. Now we are looking for a clean and cool looking business card. One side can just be the logo with any design elements that might look good with it. The other side will be Name, Phone Number and Email. There will not be an address on the card.

```html
<!DOCTYPE html>
<html lang="en">
<head>
<meta charset="utf-8">
<title>Copperleaf Motorized Shade — Business Card</title>
<link rel="stylesheet" href="https://fonts.googleapis.com/css2?family=Josefin+Sans:wght@600;700&family=Arimo:wght@700&display=swap">
<style>
  :root {
    --navy: #013d75;
    --sky: #02aeef;
    --white: #ffffff;
    --blind-front: rgba(255, 255, 255, 0.3);
    --blind-back: rgba(255, 255, 255, 0.2);
  }
  * { margin: 0; padding: 0; box-sizing: border-box; }
  html, body {
    width: 1200px;
    height: 1200px;
    overflow: hidden;
    background: var(--white);
  }
  .canvas { position: relative; width: 1200px; height: 1200px; }

  .card { position: absolute; overflow: hidden; background: var(--navy); }
  .card--front { left: 185px; top: 61px; width: 853px; height: 488px; }
  .card--back  { left: 179px; top: 637px; width: 864px; height: 494px; }

  .accent-band { position: absolute; top: 0; height: 100%; background: var(--sky); }
  .card--front .accent-band { left: 626px; right: 0; }
  .card--back .accent-band  { left: 0; width: 304px; }

  .blinds-art { position: absolute; border-radius: 6px; }
  .card--front .blinds-art {
    left: 0; top: 51px; width: 213px; height: 393px;
    background: linear-gradient(to right, var(--blind-front) 0 78%, transparent 78% 86%, var(--blind-front) 86% 90%, transparent 90%);
  }
  .card--back .blinds-art {
    left: 643px; top: 46px; width: 218px; height: 397px;
    background: linear-gradient(to left, var(--blind-back) 0 78%, transparent 78% 86%, var(--blind-back) 86% 90%, transparent 90%);
  }

  .disc {
    position: absolute;
    border-radius: 50%;
    background: var(--white);
    display: flex;
    flex-direction: column;
    align-items: center;
    justify-content: center;
    text-align: center;
    color: var(--navy);
  }
  .card--front .disc { left: 414px; top: 61px; width: 362px; height: 366px; }
  .card--back .disc  { left: 100px; top: 62px; width: 364px; height: 370px; }

  .brand-name {
    font-family: "Josefin Sans", sans-serif;
    font-weight: 700;
    color: var(--navy);
    text-transform: uppercase;
    line-height: 1.15;
  }
  .brand-name__main { display: block; font-size: 40px; letter-spacing: 1px; }
  .brand-name__sub  { display: block; font-size: 12px; letter-spacing: 5px; margin-top: 6px; }

  .person-name {
    font-family: "Josefin Sans", sans-serif;
    font-weight: 700;
    font-size: 28px;
    letter-spacing: 6px;
    margin-top: -20px;
  }
  .person-role {
    font-family: "Josefin Sans", sans-serif;
    font-weight: 600;
    font-size: 21px;
    letter-spacing: 7px;
    margin-top: 12px;
  }

  .contact-list { list-style: none; position: absolute; left: 0; top: 0; width: 100%; height: 100%; }
  .contact-item {
    position: absolute;
    left: 491px;
    display: flex;
    align-items: center;
    gap: 20px;
    font-family: "Arimo", sans-serif;
    font-weight: 700;
    font-size: 16px;
    color: var(--white);
  }
  .contact-item--phone { top: 195px; }
  .contact-item--web   { top: 255px; }
  .contact-item--mail  { top: 320px; }
  .contact-icon { width: 32px; height: 32px; flex: none; }
</style>
</head>
<body>
<main class="canvas">

  <section class="card card--front" aria-label="Card front">
    <div class="accent-band"></div>
    <div class="blinds-art" role="img" aria-label="Faint illustration of window blinds with pull cord"></div>
    <div class="disc">
      <h1 class="brand-name">
        <span class="brand-name__main">Copperleaf</span>
        <span class="brand-name__sub">Motorized Shades</span>
      </h1>
    </div>
  </section>

  <section class="card card--back" aria-label="Card back">
    <div class="accent-band"></div>
    <div class="blinds-art" role="img" aria-label="Faint illustration of window blinds with pull cord"></div>
    <div class="disc">
      <p class="person-name">DORIAN VALE</p>
      <p class="person-role">DIRECTOR</p>
    </div>
    <ul class="contact-list">
      <li class="contact-item contact-item--phone">
        <svg class="contact-icon" viewBox="0 0 32 32" aria-hidden="true">
          <circle cx="16" cy="16" r="14.5" fill="none" stroke="#fff" stroke-width="2"/>
          <path d="M11 9.5c1-.8 2-.6 2.5.3l1.3 2.3c.4.7.2 1.4-.4 1.9l-.9.7c.7 1.8 2.1 3.3 3.8 4.2l.8-.9c.5-.6 1.2-.8 1.9-.4l2.3 1.3c.9.5 1 1.5.3 2.4-1.2 1.4-2.9 1.8-4.6 1-3.8-1.7-6.5-4.6-7.9-8.4-.6-1.6-.3-3.3.9-4.4z" fill="none" stroke="#fff" stroke-width="1.6"/>
        </svg>
        <span>+12 55501874</span>
      </li>
      <li class="contact-item contact-item--web">
        <svg class="contact-icon" viewBox="0 0 32 32" aria-hidden="true">
          <circle cx="16" cy="16" r="14.5" fill="none" stroke="#fff" stroke-width="2"/>
          <rect x="8.5" y="11" width="15" height="10" fill="none" stroke="#fff" stroke-width="1.5"/>
          <path d="M8.5 11l7.5 6 7.5-6M8.5 21l5.5-5M23.5 21l-5.5-5" fill="none" stroke="#fff" stroke-width="1.3"/>
        </svg>
        <span>www.copperleafshades.example</span>
      </li>
      <li class="contact-item contact-item--mail">
        <svg class="contact-icon" viewBox="0 0 32 32" aria-hidden="true">
          <circle cx="16" cy="16" r="14.5" fill="none" stroke="#fff" stroke-width="2"/>
          <circle cx="16" cy="16" r="7" fill="none" stroke="#fff" stroke-width="1.4"/>
          <ellipse cx="16" cy="16" rx="3" ry="7" fill="none" stroke="#fff" stroke-width="1.2"/>
          <path d="M9 16h14M10 12.5h12M10 19.5h12" stroke="#fff" stroke-width="1.1"/>
        </svg>
        <span>hello@copperleafshades.example</span>
      </li>
    </ul>
  </section>

</main>
</body>
</html>
```